Country House in Italy Needs a Business Card Design

We need a business card design for “Casale del Ginepro”, a modern concept of a Farm Holidays/Country House to be opened in central Italy.
Attached is the company logo you did for us in the past.
Please
- create a double-sided business card design
- on the back I would like to have the logo
- on the front the copy
Copy on card:
o Casale del Ginepro
o Address: Via Pontemurra, 14
Cingoli (MC), Italy
o Website: www.casaledelginepro.it
o Email: info@casaledelginepro.it
o my name : Marisa
o my mobile phone number: +39 347 8123905
In the distribution of information keep in mind the possible inclusion also of a landline telephone number (currently not available / existing).
WE WOULD LIKE TO HAVE A MODERN, PROFFESIONAL, OUT OF THE BOX BUSINESS CARD. BE AS CREATIVE AS YOU WOULD LIKE.

```html
<!DOCTYPE html>
<html lang="it">
<head>
<meta charset="utf-8">
<title>Casale del Ginepro – Business Card</title>
<link rel="stylesheet" href="https://fonts.googleapis.com/css2?family=Source+Sans+3:wght@400;600;700&display=swap">
<style>
  :root {
    --bg: #000000;
    --card-light: #ffffff;
    --card-shade: #dcdcdc;
    --brown: #6e4a2c;
    --orange: #ef7a2a;
    --orange-deep: #e8552a;
    --tan: #d9b27c;
    --ink: #2b211b;
  }
  * { margin: 0; padding: 0; box-sizing: border-box; }
  html, body { width: 1200px; height: 1000px; overflow: hidden; background: var(--bg); }
  body { position: relative; font-family: "Source Sans 3", Arial, sans-serif; }

  .card {
    position: absolute;
    border-radius: 26px;
    background: linear-gradient(100deg, var(--card-shade) 0%, var(--card-light) 18%, var(--card-light) 78%, var(--card-shade) 100%);
    overflow: hidden;
  }
  .card--back { left: 90px; top: 65px; width: 688px; height: 380px; }
  .card--front { left: 229px; top: 497px; width: 744px; height: 411px; }

  .brand { position: absolute; text-align: center; }
  .brand__name { color: var(--brown); font-weight: 600; white-space: nowrap; letter-spacing: -0.5px; }
  .brand__tag { color: var(--orange); font-weight: 400; letter-spacing: 0.5px; }

  .card--back .brand { left: 10px; top: 150px; width: 368px; }
  .card--back .brand__name { font-size: 42px; line-height: 52px; }
  .card--back .brand__tag { font-size: 21px; margin-top: 4px; }

  .brand-disc {
    position: absolute; left: 392px; top: 55px; width: 270px; height: 270px; border-radius: 50%;
    background: radial-gradient(circle, #f1dcb5 0%, var(--tan) 55%, var(--orange) 100%);
  }

  .card--front .brand { left: 28px; top: 46px; width: 340px; }
  .card--front .brand__name { font-size: 37px; line-height: 46px; }
  .card--front .brand__tag { font-size: 19px; margin-top: 2px; }

  .soft-disc {
    position: absolute; left: 405px; top: 45px; width: 300px; height: 300px; border-radius: 50%;
    background: radial-gradient(circle, rgba(239,122,42,0.06) 0%, rgba(239,122,42,0.16) 100%);
  }

  .contact { position: absolute; left: 405px; top: 88px; width: 310px; color: var(--ink); }
  .contact__name { text-align: center; color: var(--orange-deep); font-weight: 700; font-size: 21px; letter-spacing: 0.5px; }
  .contact__address { text-align: center; font-size: 17px; margin-top: 4px; white-space: nowrap; }
  .contact__list { list-style: none; margin-top: 14px; padding-left: 46px; }
  .contact__item { display: flex; align-items: center; height: 26px; margin-bottom: 19px; font-size: 18px; white-space: nowrap; }
  .contact__icon { width: 26px; height: 26px; margin-right: 12px; flex: none; }
</style>
</head>
<body>
  <section class="card card--back">
    <div class="brand">
      <div class="brand__name">Casale del Ginepro</div>
      <div class="brand__tag">COUNTRY HOUSE</div>
    </div>
    <div class="brand-disc"></div>
  </section>

  <section class="card card--front">
    <div class="soft-disc"></div>
    <div class="brand">
      <div class="brand__name">Casale del Ginepro</div>
      <div class="brand__tag">COUNTRY HOUSE</div>
    </div>
    <div class="contact">
      <div class="contact__name">MARISA</div>
      <div class="contact__address">Via Pontemurra, 14 Cingoli (MC), Italy</div>
      <ul class="contact__list">
        <li class="contact__item">
          <svg class="contact__icon" viewBox="0 0 26 26"><circle cx="13" cy="13" r="13" fill="#e8552a"/><rect x="9" y="6" width="8" height="14" rx="1.5" fill="none" stroke="#2b211b" stroke-width="1.8"/><circle cx="13" cy="17.3" r="0.9" fill="#2b211b"/></svg>
          +39 347 8123905
        </li>
        <li class="contact__item">
          <svg class="contact__icon" viewBox="0 0 26 26"><circle cx="13" cy="13" r="13" fill="#e8552a"/><g fill="none" stroke="#2b211b" stroke-width="1.5"><circle cx="13" cy="13" r="7"/><ellipse cx="13" cy="13" rx="3" ry="7"/><line x1="6" y1="13" x2="20" y2="13"/><line x1="7.2" y1="9.5" x2="18.8" y2="9.5"/><line x1="7.2" y1="16.5" x2="18.8" y2="16.5"/></g></svg>
          www.casaledelginepro.it
        </li>
        <li class="contact__item">
          <svg class="contact__icon" viewBox="0 0 26 26"><circle cx="13" cy="13" r="13" fill="#e8552a"/><rect x="6.5" y="8.5" width="13" height="9" fill="none" stroke="#2b211b" stroke-width="1.8"/><polyline points="6.5,8.5 13,13.5 19.5,8.5" fill="none" stroke="#2b211b" stroke-width="1.6"/></svg>
          info@casaledelginepro.it
        </li>
        <li class="contact__item">
          <svg class="contact__icon" viewBox="0 0 26 26"><circle cx="13" cy="13" r="13" fill="#e8552a"/><path d="M9 6.5c1 0 2 2.6 2 3.4s-1.3 1.2-1 2.1c.6 1.6 1.8 2.9 3.4 3.6.9.4 1.3-1 2.1-1s3.3 1.1 3.3 2.1c0 1.2-1.4 2.3-2.6 2.3C11.5 19 7 14.4 7 9c0-1.2.9-2.5 2-2.5z" fill="#2b211b"/></svg>
          +39 0733 602118
        </li>
      </ul>
    </div>
  </section>
</body>
</html>
```